Fire Risk Assessment App needs a sleek UI design

I need a sleek, modern but professional design for my 5 page Fire Risk Assessment App. Include gradient background, fire themed colours including reds, yellows, light orange and a touch of black. Design must ooze simplicity and professionalism. This is for the UK market. See attached images and word doc for more information.

Target Market(s)

General public and business owners

Industry/Entity Type

Technology / Fire Safety

Colors
00AB8E
00BBA5
67D7C9
C6EFE9
E9F9F6
59FF00
82FF00
B8FF75
E3FFCB
F4FFEA
FFC000
F8CF3A
FAE287
FDF2CF
FEFAEE
F0912C
F2A743
F7CA91
FBE8D2
FDF5EE
EE7325
F08F49
F5BC92
FAE3D3
FDF4ED
EB3D1F
EC4F4E
F09395
F8D3D4
FCEDEE

```html
<!DOCTYPE html>
<html lang="en">
<head>
<meta charset="UTF-8">
<title>Purchase – Fire Risk Assessment</title>
<link href="https://fonts.googleapis.com/css2?family=Epilogue:wght@400;500;600&display=swap" rel="stylesheet">
<style>
  :root {
    --backdrop: #20233a;
    --ink: #1f2236;
    --ink-soft: #55586a;
    --cream-top: #fef9ec;
    --cream-bottom: #fdeeb4;
    --nav-bg: #f5e6b3;
    --orange: #f0912c;
    --orange-deep: #ee7325;
    --red: #eb3d1f;
    --yellow: #ffc000;
    --white: #ffffff;
    --ring: #fde3c4;
  }
  * { box-sizing: border-box; margin: 0; padding: 0; }
  html, body {
    width: 1200px; height: 1200px; overflow: hidden;
    background: var(--backdrop);
    font-family: "Epilogue", sans-serif;
  }
  .screen {
    position: absolute; left: 373px; top: 107px;
    width: 455px; height: 985px;
    background: linear-gradient(180deg, var(--cream-top) 0%, var(--cream-bottom) 100%);
    overflow: hidden;
  }
  .page-title {
    position: absolute; top: 66px; width: 100%; text-align: center;
    font-size: 31px; font-weight: 400; color: var(--ink);
  }
  .page-subtitle {
    position: absolute; top: 105px; width: 100%; text-align: center;
    font-size: 16.5px; color: var(--ink-soft);
  }
  .plan-panel {
    position: absolute; left: 19px; top: 151px; width: 416px; height: 726px;
    border-radius: 31px;
    background:
      linear-gradient(200deg, var(--red) 0%, rgba(238,115,37,0.6) 30%, rgba(240,145,44,0) 60%),
      linear-gradient(20deg, var(--yellow) 0%, var(--orange) 45%, var(--orange-deep) 100%);
  }
  .panel-heading {
    position: absolute; top: 29px; width: 100%; text-align: center;
    color: var(--white); font-size: 19.5px; font-weight: 500; line-height: 23px;
  }
  .plan-card {
    position: absolute; left: 21px; width: 374px; height: 123px;
    border-radius: 19px; color: var(--white); text-align: center;
    overflow: hidden;
  }
  .plan-card::before {
    content: ""; position: absolute; inset: 0;
    background: linear-gradient(90deg, rgba(255,214,140,0.35), rgba(255,200,150,0.2));
  }
  .plan-card.bronze { top: 100px; background: linear-gradient(180deg, #ffb884 0%, #f9a64e 45%, #f49042 100%); }
  .plan-card.silver { top: 233px; background: linear-gradient(180deg, #cfc5bf 0%, #f7a24a 45%, #f39542 100%); }
  .plan-card.gold { top: 367px; background: linear-gradient(180deg, #f2c95a 0%, #f8b444 45%, #f5a040 100%); }
  .plan-card.platinum { top: 500px; background: linear-gradient(180deg, #cfc6c2 0%, #f9bc3e 45%, #f7a33c 100%); }
  .plan-card > * { position: absolute; left: 0; width: 100%; }
  .radio {
    left: 16px !important; top: 16px; width: 30px !important; height: 30px;
    border: 2px solid var(--ring); border-radius: 50%;
  }
  .plan-name { font-size: 17px; font-weight: 500; }
  .plan-detail { font-size: 13.5px; opacity: 0.95; }
  .plan-was { font-size: 14px; text-decoration: line-through; opacity: 0.85; }
  .plan-price { font-size: 17px; font-weight: 600; }
  .bronze .plan-name { top: 27px; } .bronze .plan-detail { top: 52px; } .bronze .plan-price { top: 74px; }
  .stacked .plan-name { top: 16px; }
  .stacked .plan-detail { top: 41px; }
  .stacked .plan-was { top: 62px; }
  .stacked .plan-price { top: 87px; }
  .checkout {
    position: absolute; left: 21px; top: 644px; width: 374px; height: 56px;
    border-radius: 28px;
    background: linear-gradient(90deg, var(--red) 0%, #ed6a2c 100%);
    box-shadow: 0 8px 16px rgba(180,60,20,0.3);
    color: var(--white); font-size: 17px; text-align: center; line-height: 57px;
  }
  .checkout-icon {
    position: absolute; left: 5px; top: 4px; width: 48px; height: 48px; border-radius: 50%;
    background: linear-gradient(135deg, #f49a3a, var(--orange-deep));
    display: flex; align-items: center; justify-content: center;
  }
  .checkout-label { padding-left: 20px; }
  .tab-bar {
    position: absolute; left: 0; top: 903px; width: 100%; height: 82px;
    background: linear-gradient(90deg, #f9ebbe, var(--nav-bg) 60%, #efdb9c);
  }
  .tab-indicator {
    position: absolute; left: 146px; top: 0; width: 51px; height: 4px;
    border-radius: 0 0 3px 3px; background: var(--orange-deep);
  }
  .tab-icon { position: absolute; top: 26px; width: 30px; height: 30px; }
</style>
</head>
<body>
  <main class="screen">
    <h1 class="page-title">Purchase</h1>
    <p class="page-subtitle">Lorem Ipsum is simply dummy text</p>

    <section class="plan-panel">
      <h2 class="panel-heading">FIRE RISK ASSESSMENT<br>PAYMENT OPTIONS</h2>

      <div class="plan-card bronze">
        <span class="radio"></span>
        <div class="plan-name">BRONZE</div>
        <div class="plan-detail">1 Fire Risk Assessment</div>
        <div class="plan-price">£19.99</div>
      </div>
      <div class="plan-card silver stacked">
        <span class="radio"></span>
        <div class="plan-name">SILVER</div>
        <div class="plan-detail">3 Fire Risk Assessment</div>
        <div class="plan-was">£59.97</div>
        <div class="plan-price">£54.99</div>
      </div>
      <div class="plan-card gold stacked">
        <span class="radio"></span>
        <div class="plan-name">GOLD</div>
        <div class="plan-detail">5 Fire Risk Assessment</div>
        <div class="plan-was">£99.95</div>
        <div class="plan-price">£89.99</div>
      </div>
      <div class="plan-card platinum stacked">
        <span class="radio"></span>
        <div class="plan-name">PLATINUM</div>
        <div class="plan-detail">10 Fire Risk Assessment</div>
        <div class="plan-was">£199.90</div>
        <div class="plan-price">£174.99</div>
      </div>

      <div class="checkout">
        <span class="checkout-icon">
          <svg width="20" height="20" viewBox="0 0 20 20">
            <path d="M7 5V3.5A1.5 1.5 0 0 1 8.5 2h3A1.5 1.5 0 0 1 13 3.5V5" fill="none" stroke="#fff" stroke-width="1.8"/>
            <rect x="1.5" y="5" width="17" height="13" rx="2.5" fill="#fff"/>
          </svg>
        </span>
        <span class="checkout-label">Checkout</span>
      </div>
    </section>

    <nav class="tab-bar">
      <span class="tab-indicator"></span>
      <svg class="tab-icon" style="left:45px" viewBox="0 0 30 30">
        <path d="M5 24 A12 12 0 1 1 25 24" fill="none" stroke="#1f2236" stroke-width="5" stroke-dasharray="6 2.2"/>
        <path d="M15 9 L16.6 20 A1.7 1.7 0 0 1 13.4 20 Z" fill="#1f2236"/>
      </svg>
      <svg class="tab-icon" style="left:156px" viewBox="0 0 30 30">
        <rect x="2" y="4" width="26" height="22" rx="4" fill="#ee5a28"/>
        <rect x="2" y="10" width="26" height="3" fill="#f9ebbe"/>
        <rect x="6" y="19" width="5" height="2" fill="#f9ebbe"/>
        <rect x="13" y="19" width="5" height="2" fill="#f9ebbe"/>
      </svg>
      <svg class="tab-icon" style="left:268px" viewBox="0 0 30 30">
        <path d="M6 3h18a4 4 0 0 1 4 4v11a4 4 0 0 1-4 4h-5l-4 5v-5H6a4 4 0 0 1-4-4V7a4 4 0 0 1 4-4z" fill="#1f2236"/>
        <rect x="10" y="11" width="10" height="2.4" rx="1.2" fill="#f5e6b3"/>
      </svg>
      <svg class="tab-icon" style="left:380px" viewBox="0 0 30 30">
        <circle cx="11" cy="7" r="5.5" fill="#1f2236"/>
        <path d="M2 28v-6a6 6 0 0 1 6-6h7a6 6 0 0 1 4 1.5V28z" fill="#1f2236"/>
        <path d="M17 27v-3a4 4 0 0 1 4-4h7M24.5 16.5 28 20l-3.5 3.5" fill="none" stroke="#1f2236" stroke-width="2"/>
      </svg>
    </nav>
  </main>
</body>
</html>
```